New Business Card Design Project

I need a meaningful new business card. Therefore, the website should convey growth, joy, uniqueness, workout and a bit of luxury.
Color scheme should be petrol, gold and matching colors.

```html
<!DOCTYPE html>
<html lang="en">
<head>
<meta charset="utf-8">
<title>Lumen Core Studio – Business Card</title>
<link href="https://fonts.googleapis.com/css2?family=Great+Vibes&family=Montserrat:wght@400;500&display=swap" rel="stylesheet">
<style>
  :root {
    --petrol: #17a89f;
    --gold: #c9a24a;
    --gold-light: #e6cb85;
    --ink: #1f1f1f;
    --card: #ffffff;
    --backdrop: #1d1d1d;
  }
  * { box-sizing: border-box; margin: 0; padding: 0; }
  html, body { width: 1200px; height: 1059px; overflow: hidden; }
  body {
    background: var(--backdrop);
    position: relative;
    font-family: "Montserrat", Arial, sans-serif;
    color: var(--ink);
  }
  .card {
    position: absolute;
    background: var(--card);
    border-radius: 24px;
    overflow: hidden;
  }
  .card--front { left: 257px; top: 87px; width: 688px; height: 393px; }
  .card--back  { left: 252px; top: 546px; width: 710px; height: 401px; }

  .brand {
    position: absolute;
    display: flex;
    flex-direction: column;
    align-items: center;
    text-align: center;
    color: var(--petrol);
    font-weight: 500;
    letter-spacing: 0.04em;
  }
  .brand__dot {
    border-radius: 50%;
    background: radial-gradient(circle at 35% 30%, var(--gold-light), var(--gold) 70%);
  }
  .card--front .brand { left: 110px; top: 118px; width: 230px; font-size: 27px; line-height: 1.2; }
  .card--front .brand__dot { width: 46px; height: 46px; margin-bottom: 16px; }
  .card--back .brand { left: 195px; top: 100px; width: 320px; font-size: 42px; line-height: 1.2; }
  .card--back .brand__dot { width: 72px; height: 72px; margin-bottom: 24px; }

  .divider {
    position: absolute;
    left: 348px; top: 104px;
    width: 2px; height: 215px;
    background: var(--petrol);
  }
  .contact { position: absolute; left: 364px; top: 100px; width: 300px; }
  .contact__name {
    font-family: "Great Vibes", cursive;
    color: var(--petrol);
    font-size: 32px;
    line-height: 1;
  }
  .contact__role { font-size: 15px; margin-top: 2px; }
  .contact__address { font-size: 15px; line-height: 18px; margin-top: 28px; padding-left: 2px; }
  .contact__list { list-style: none; margin-top: 26px; padding-left: 2px; }
  .contact__item {
    display: flex; align-items: center;
    font-size: 15px; height: 24.5px;
  }
  .contact__icon { width: 14px; height: 14px; margin-right: 14px; fill: var(--petrol); }
</style>
</head>
<body>
  <section class="card card--front">
    <div class="brand">
      <span class="brand__dot"></span>
      <span class="brand__name">Lumen Core<br>Studio</span>
    </div>
    <div class="divider"></div>
    <div class="contact">
      <p class="contact__name">Maren Castell</p>
      <p class="contact__role">Owner</p>
      <p class="contact__address">418 Linden Park Ave, #12<br>Fairhaven, OH 43190</p>
      <ul class="contact__list">
        <li class="contact__item">
          <svg class="contact__icon" viewBox="0 0 14 14"><path d="M1 5c0-2 2.5-3 6-3s6 1 6 3v1h-3V4.5H4V6H1z"/><rect x="2.5" y="7" width="9" height="6" rx="1"/></svg>
          0412557908
        </li>
        <li class="contact__item">
          <svg class="contact__icon" viewBox="0 0 14 14"><rect x="0" y="3" width="14" height="9" rx="1"/><path d="M0 3.5 7 8l7-4.5" stroke="#fff" stroke-width="1.2" fill="none"/></svg>
          hello@lumencorestudio.com
        </li>
        <li class="contact__item">
          <svg class="contact__icon" viewBox="0 0 14 14"><circle cx="7" cy="7" r="6.5"/><path d="M1 7h12M7 .5c-3 3-3 10 0 13M7 .5c3 3 3 10 0 13" stroke="#fff" stroke-width="0.9" fill="none"/></svg>
          www.lumencorestudio.com
        </li>
      </ul>
    </div>
  </section>

  <section class="card card--back">
    <div class="brand">
      <span class="brand__dot"></span>
      <span class="brand__name">Lumen Core<br>Studio</span>
    </div>
  </section>
</body>
</html>
```